I need a SEO-friendly Wordpress website (making sure to style H1, H2, H3, etc correctly) for a Hawaii-based law firm called Meridale Crown Legal Group. Comparable websites include https://brvtlaw.com/ and https://www.lorvin.com/ for design reference. The current copy on the TuvellAttorney.com website can be used.

Coding

Coded - Design and coding required

```html
<!DOCTYPE html>
<html lang="en">
<head>
<meta charset="utf-8">
<title>Meridale Crown Legal Group — Divorce and Personal Injury Lawyers</title>
<link href="https://fonts.googleapis.com/css2?family=Montserrat:wght@500;600;700;800&family=Open+Sans:wght@400;600;700&family=Noto+Serif:ital@1&display=swap" rel="stylesheet">
<style>
:root{
  --red:#b84a3c;
  --red-dark:#7e2b22;
  --gold:#bb9e72;
  --ink:#2b2b2b;
  --text:#555;
  --rule:#e6e6e6;
  --night:#141414;
  --footer:#232323;
  --footer-base:#1c1c1c;
  --field:#2f2f2f;
  --map:#e8eae6;
  --sea:#aacbf2;
}
*{box-sizing:border-box;margin:0;padding:0}
html,body{width:1200px;height:2906px;overflow:hidden;background:#fff}
body{position:relative;font-family:"Open Sans",sans-serif;color:var(--text)}
.abs{position:absolute}
a{color:inherit;text-decoration:none}

/* top bar */
.topbar{left:0;top:0;width:1200px;height:36px;background:var(--red);color:#fff;font-size:10px}
.topbar .mail{left:234px;top:12px;display:flex;gap:6px;align-items:center}
.topbar .addr{left:571px;top:12px;display:flex;gap:6px;align-items:center}
.topbar .direction{left:858px;top:0;width:342px;height:36px;background:var(--red-dark);clip-path:polygon(12px 0,100% 0,100% 100%,0 100%);font:600 11px "Montserrat",sans-serif;padding:12px 0 0 25px}

/* header */
.brand{left:233px;top:64px}
.brand-name{font:700 16px "Montserrat",sans-serif;color:var(--red);letter-spacing:.2px}
.brand-tag{font:italic 12px "Noto Serif",serif;color:var(--gold);margin-top:4px;letter-spacing:.4px}
.call{left:755px;top:58px;display:flex;gap:12px}
.call-text{font:italic 12px "Noto Serif",serif;color:var(--ink)}
.call-num{font:700 19px "Montserrat",sans-serif;color:var(--gold);margin:3px 0 0 5px}
.header-rule{left:0;top:117px;width:1200px;height:1px;background:var(--rule)}

.nav{left:233px;top:134px;display:flex;gap:27px;font:500 10px "Open Sans",sans-serif;color:#222}
.nav .active{color:var(--red)}
.consult{left:804px;top:117px;width:162px;height:43px;background:var(--red-dark);color:#fff;font:600 11px "Open Sans",sans-serif;text-align:center;line-height:43px}

/* hero */
.hero{left:0;top:160px;width:1200px;height:375px;background:linear-gradient(100deg,#6b4a2b 0%,#2f3540 32%,#3a3f4a 55%,#6a5142 72%,#c9c9c9 100%)}
.hero-card{left:403px;top:254px;width:393px;height:189px;background:rgba(184,74,60,.92);color:#fff;text-align:center;padding:9px}
.hero-card .frame{border:1px solid rgba(255,255,255,.6);height:100%;padding:18px 20px 0}
.hero-card p{font-size:11.5px;font-weight:600}
.hero-card .lead{font-size:15.5px;font-weight:700;line-height:19px;margin:4px 0 18px}

/* about */
.eyebrow-bar{left:233px;top:597px;width:2px;height:42px;background:var(--red)}
.eyebrow{font:600 11px "Open Sans",sans-serif;color:var(--red)}
.about-head{left:249px;top:597px}
.about-head h2{font:700 20px "Open Sans",sans-serif;color:var(--ink);margin-top:8px}
.about-sub{left:234px;top:666px;font:700 14px "Open Sans",sans-serif;color:var(--red)}
.about-copy{left:234px;top:701px;width:419px;font-size:9px;line-height:15px;text-align:justify}
.about-copy p+p{margin-top:15px}
.btn-gold{background:var(--gold);color:#fff;font:600 9px "Open Sans",sans-serif;text-align:center}
.about-btn{left:234px;top:855px;width:128px;height:28px;line-height:28px}
.enquiry{left:375px;top:851px;border-left:1px solid var(--rule);padding-left:15px;height:36px}
.enquiry small{display:block;font:600 9.5px "Open Sans",sans-serif;color:var(--ink)}
.enquiry strong{font:700 14px "Montserrat",sans-serif;color:var(--gold)}
.about-photo{left:671px;top:597px;width:295px;height:290px;background:linear-gradient(160deg,#8c8e93,#3b3f48 45%,#b49263 80%,#6a4a2e)}
.about-photo .inset{position:absolute;inset:13px;border:1px solid rgba(255,255,255,.7)}

/* stats */
.stats{left:0;top:942px;width:1200px;height:238px;background:linear-gradient(90deg,#2a2520 0%,#0f0f0f 25%,#0c0c0c 75%,#2a2a2a 100%)}
.stat{top:1000px;display:flex;gap:13px;color:#fff}
.stat .rule{width:2px;height:40px;background:var(--gold)}
.stat b{display:block;font:800 34px "Montserrat",sans-serif;line-height:34px}
.stat span{font:700 11.5px "Montserrat",sans-serif}
.panel{left:233px;top:1110px;width:733px;height:90px;background:#fff}

/* section titles */
.section-title{left:0;width:1200px;text-align:center}
.section-title .kicker{display:inline-flex;align-items:center;gap:13px;font:600 11px "Open Sans",sans-serif;color:var(--red)}
.section-title .kicker::before,.section-title .kicker::after{content:"";width:37px;height:1px;background:var(--red)}
.section-title h2{font:700 20px "Open Sans",sans-serif;color:var(--ink);margin-top:8px;letter-spacing:.3px}

/* practice */
.area{top:1251px;width:169px;height:143px;display:flex;align-items:center;justify-content:center;text-align:center;color:#fff;font:700 12px "Montserrat",sans-serif;padding:0 25px}
.area.family{left:233px;background:linear-gradient(135deg,#c9b08a,#a98e66)}
.area.injury{left:421px;background:linear-gradient(135deg,#bfa57d,#9c8259)}
.area.corporate{left:608px;background:linear-gradient(135deg,#c8b293,#a89070)}
.area.estate{left:795px;background:linear-gradient(180deg,#c6b693,#8c8a5e)}

/* blog */
.post{top:1544px;width:357px;height:285px;background:#fff;box-shadow:0 0 6px rgba(0,0,0,.13);padding:0 22px 0 26px}
.post .accent{position:absolute;left:26px;top:0;width:12px;height:81px;background:var(--gold)}
.post h3{margin:18px 0 0 28px;font:600 20px "Open Sans",sans-serif;color:var(--ink);line-height:27px}
.post p{margin-top:24px;font-size:10px;line-height:16px}
.post .more{display:block;margin-top:14px;font:italic 10px "Noto Serif",serif;color:var(--gold)}
.read-blog{left:554px;top:1885px;width:108px;height:42px;background:var(--red);color:#fff;font:700 12px "Montserrat",sans-serif;text-align:center;line-height:42px;box-shadow:0 2px 5px rgba(0,0,0,.25)}

/* map & footer */
.map{left:0;top:2001px;width:1200px;height:405px;background:linear-gradient(90deg,var(--sea) 0%,var(--sea) 22%,var(--map) 30%,var(--map) 100%)}
.gold-line{left:0;top:2406px;width:1200px;height:8px;background:var(--gold)}
.footer{left:0;top:2414px;width:1200px;height:406px;background:var(--footer)}
.footer-base{left:0;top:2820px;width:1200px;height:86px;background:var(--footer-base);border-top:1px solid #333;text-align:center;padding-top:37px;font-size:9px;color:#888}
.f-brand{left:233px;top:2486px}
.f-links{left:250px;top:2541px;display:grid;grid-template-columns:132px 110px;row-gap:14px;font-size:11px;color:#ccc}
.f-links li{list-style:none;display:flex;align-items:center;gap:9px;border-bottom:1px solid #2f2f2f;padding-bottom:9px}
.f-links li::before{content:"";border-left:4px solid var(--gold);border-top:3px solid transparent;border-bottom:3px solid transparent}
.f-heading{font:700 14px "Montserrat",sans-serif;color:#fff}
.follow{left:233px;top:2665px;width:295px;border-bottom:1px solid #3a3a3a;padding-bottom:6px}
.socials{left:236px;top:2702px;display:flex;gap:8px}
.socials span{width:38px;height:38px;border-radius:50%;background:#333}
.reach{left:546px;top:2486px;width:420px;border-bottom:1px solid #3a3a3a;padding-bottom:6px}
.field{background:var(--field);color:#9a9a9a;font-size:8px;padding:10px 10px}
.send{left:546px;top:2713px;width:420px;height:34px;background:var(--gold);color:#fff;font:700 11px "Montserrat",sans-serif;padding:11px 18px;display:flex;justify-content:space-between}
</style>
</head>
<body>

<div class="abs topbar">
  <div class="abs mail">
    <svg width="10" height="8" viewBox="0 0 10 8"><rect x=".5" y=".5" width="9" height="7" fill="none" stroke="#fff"/><path d="M.5 .5 5 4.5 9.5 .5" fill="none" stroke="#fff"/></svg>
    clients@tuvellattorney.com
  </div>
  <div class="abs addr">
    <svg width="8" height="10" viewBox="0 0 8 10"><path d="M4 9.5C1.5 6 .5 4.7.5 3.5a3.5 3.5 0 0 1 7 0C7.5 4.7 6.5 6 4 9.5z" fill="none" stroke="#fff"/><circle cx="4" cy="3.5" r="1.2" fill="#fff"/></svg>
    48-2210 Palani Road, Suite 302, Kailua Kona, Hawaii 96740.
  </div>
  <a class="abs direction" href="#map">Get Direction &nbsp;⟶</a>
</div>

<header>
  <div class="abs brand">
    <div class="brand-name">MERIDALE CROWN LEGAL GROUP</div>
    <div class="brand-tag">Divorce and Personal Injury Lawyers</div>
  </div>
  <div class="abs call">
    <svg width="34" height="34" viewBox="0 0 34 34"><circle cx="17" cy="17" r="15.5" fill="none" stroke="#bb9e72" stroke-width="1.5"/><path d="M12 10c1 0 2 2.5 2.5 3.5s-1.5 1.5-1 2.5 2.5 3.5 3.5 4 1.5-1.5 2.5-1 3.5 1.5 3.5 2.5-1.5 2.5-3 2.5C15 24 10 19 10 13c0-1.5 1-3 2-3z" fill="none" stroke="#bb9e72" stroke-width="1.4"/></svg>
    <div>
      <div class="call-text">Call For Your Free Appointment</div>
      <div class="call-num">+1.808.555.0148</div>
    </div>
  </div>
  <div class="abs header-rule"></div>
  <nav class="abs nav">
    <a class="active" href="#">HOME</a><a href="#">ABOUT US</a><a href="#">PRACTICE AREAS</a><a href="#">ATTORNEYS</a><a href="#">BLOG</a><a href="#">CONTACT US</a>
  </nav>
  <a class="abs consult" href="#">FREE CONSULTATION</a>
</header>

<section>
  <div class="abs hero" role="img" aria-label="Close view of a lawyer in a suit holding an open law book beside a wooden gavel"></div>
  <div class="abs hero-card">
    <div class="frame">
      <p>Kona Lawyers of MCLG -Legal kōkua with aloha.</p>
      <p style="margin-top:17px">Over 70 years of combined practice, specializing in:</p>
      <h1 class="lead">Personal Injury, Family &amp; Divorce<br>Child Custody</h1>
      <p>Dedicated to making sure you receive the care and attention you need.</p>
    </div>
  </div>
</section>

<section>
  <div class="abs eyebrow-bar"></div>
  <div class="abs about-head">
    <div class="eyebrow" style="margin-left:0">WHO WE ARE</div>
    <h2>ABOUT THE KONA LAWYERS OF MCLG</h2>
  </div>
  <h3 class="abs about-sub">Lawyers Serving the Big Island and Neighboring Islands</h3>
  <div class="abs about-copy">
    <p>The experienced attorneys in the Meridale Crown Legal Group's Kailua Kona, Hawaii office provide clients with a wide range of litigation expertise, including legal claims involving divorce &amp; family, personal injury, toxic exposures, intellectual property, and real estate.</p>
    <p>Our Kona office also offers commercial and hospitality litigation expertise on behalf of a wide variety of clients, including restaurants, hotels, property owners, and many others. We never wish to see our clients go to court, though if there is no other option, you're in safe hands with our seasoned trial lawyers and the many years of courtroom experience behind them.</p>
  </div>
  <a class="abs btn-gold about-btn" href="#">More About Us</a>
  <div class="abs enquiry">
    <small>For Any Enquiry and Question Please Call us 24/7</small>
    <strong>+1.808.555.0148</strong>
  </div>
  <div class="abs about-photo" role="img" aria-label="Attorney at a desk reading beside brass scales of justice"><div class="inset"></div></div>
</section>

<section>
  <div class="abs stats" role="img" aria-label="Dark backdrop with a statue of Lady Justice"></div>
  <div class="abs stat" style="left:358px"><div class="rule"></div><div><b>200+</b><span>TRUSTED CLIENTS</span></div></div>
  <div class="abs stat" style="left:575px"><div class="rule"></div><div><b>182+</b><span>SUCCESSFUL CASE</span></div></div>
  <div class="abs stat" style="left:796px"><div class="rule"></div><div><b>245+</b><span>CASE CLOSED</span></div></div>
  <div class="abs panel"></div>
</section>

<section>
  <div class="abs section-title" style="top:1172px">
    <div class="kicker">WHAT WE DO</div>
    <h2>OUR PRACTICE AREAS</h2>
  </div>
  <div class="abs area family" role="img" aria-label="Older couple at home">FAMILY &amp; DIVORCE</div>
  <div class="abs area injury" role="img" aria-label="Injured person receiving care">PERSONAL INJURY</div>
  <div class="abs area corporate" role="img" aria-label="Office tower facade">CORPORATE &amp; INTELLECTUAL PROPERTY</div>
  <div class="abs area estate" role="img" aria-label="House with a green lawn">REAL ESTATE</div>
</section>

<section>
  <div class="abs section-title" style="top:1453px">
    <div class="kicker">BLOG</div>
    <h2>FROM THE BLOG</h2>
  </div>
  <article class="abs post" style="left:233px">
    <div class="accent"></div>
    <h3>Top 10 Things to Do Before Filing for Divorce</h3>
    <p>No one gets married with the intention of things not working out, but it's an unfortunate fact that many marriages don't work out in the end.&nbsp; For those who are in troubled marriage, here are the Top 10 things you should do before filing for a divorce. And whether you're a client or not, from all of us here at Meridale Crown Legal Group, we hope that this checklist can help you through tough times.</p>
    <a class="more" href="#">Read More</a>
  </article>
  <article class="abs post" style="left:608px">
    <div class="accent"></div>
    <h3>Top 15 Things to Do During Custody Battle</h3>
    <p>It's already tragic enough when two people who planned on spending their lives together no longer wish to see that dream through, but to compound the tragedy is when children [and their custody] get caught in the crossfire.&nbsp; With that in mind, here are the top 15 things you can do to make this difficult time go as smoothly as possible, and with minimal strain put on your children</p>
    <a class="more" href="#">Read More</a>
  </article>
  <a class="abs read-blog" href="#">READ BLOG</a>
</section>

<div id="map" class="abs map" role="img" aria-label="Street map of Kailua Kona showing the office location"></div>
<div class="abs gold-line"></div>

<footer>
  <div class="abs footer"></div>
  <div class="abs f-brand">
    <div class="brand-name" style="color:#fff">MERIDALE CROWN LEGAL GROUP</div>
    <div class="brand-tag">Divorce and Personal Injury Lawyers</div>
  </div>
  <ul class="abs f-links">
    <li>Home</li><li>Attorneys</li><li>About us</li><li>Blog</li><li>Practice Areas</li><li>Contact Us</li>
  </ul>
  <div class="abs follow f-heading">FOLLOW US</div>
  <div class="abs socials" aria-label="Social links"><span></span><span></span><span></span><span></span></div>

  <div class="abs reach f-heading">REACH OUT TO US</div>
  <div class="abs field" style="left:546px;top:2527px;width:204px;height:30px">First Name</div>
  <div class="abs field" style="left:762px;top:2527px;width:204px;height:30px">Last Name</div>
  <div class="abs field" style="left:546px;top:2570px;width:204px;height:30px">Email</div>
  <div class="abs field" style="left:762px;top:2570px;width:204px;height:30px">Subject</div>
  <div class="abs field" style="left:546px;top:2614px;width:420px;height:77px">Message</div>
  <div class="abs send">SEND MESSAGE
    <svg width="16" height="12" viewBox="0 0 16 12"><rect width="16" height="12" rx="1" fill="#fff"/><path d="M1 1 8 7l7-6" fill="none" stroke="#bb9e72" stroke-width="1.5"/></svg>
  </div>
  <div class="abs footer-base">Copyright © 2019 Meridale Crown Legal Group. All Rights Reserved</div>
</footer>

</body>
</html>
```